Web Design Project

I want customers to be able to book appointments to get their makeup done and make a deposit and also have a gallery where i put my portfolio images, i want it to be very simple yet elegant.

Target Market(s)

Women ranging from 18-40 that want to get their makeup done

Industry/Entity Type

Makeup

Font styles to use
Sans Serif
Decorative

Requirements
Nice to have
• easy scheduling option and option to pay service in full on website.

```html
<!DOCTYPE html>
<html lang="en">
<head>
<meta charset="utf-8">
<title>Makeup Artist Portfolio</title>
<link rel="stylesheet" href="https://fonts.googleapis.com/css2?family=Roboto+Condensed:wght@400;700&family=Roboto:wght@400;500;700&display=swap">
<style>
  :root{
    --red:#d8313a;
    --red-deep:#b8222a;
    --ink:#2a2a2a;
    --body:#444;
    --white:#fff;
    --topbar:#2b2624;
    --brown:#3b312d;
    --brown-panel:#34302e;
    --footer:#2f2927;
    --bottom:#2a2523;
    --grey-btn:#cfcfcf;
  }
  *{box-sizing:border-box;margin:0;padding:0}
  html,body{width:1200px;height:3097px;overflow:hidden;background:var(--white)}
  body{font-family:"Roboto",Arial,sans-serif;color:var(--body)}
  .canvas{position:relative;width:1200px;height:3097px}
  .abs{position:absolute}
  .cond{font-family:"Roboto Condensed","Arial Narrow",sans-serif;font-weight:700;text-transform:uppercase;white-space:nowrap}

  /* top bar */
  .topbar{left:0;top:0;width:1200px;height:52px;background:var(--topbar)}
  .topbar .welcome{left:95px;top:0;line-height:52px;color:var(--white);font-size:15px}
  .topbar .nav{left:636px;top:0;display:flex;gap:38px;line-height:52px;color:var(--white);font-size:15px}
  .topbar .search{left:1019px;top:0;width:181px;height:52px;background:var(--red);display:flex;align-items:center;justify-content:center}

  /* header */
  .logo{left:95px;top:92px;font-size:44px;color:var(--red);letter-spacing:.5px}
  .head-btn{top:95px;height:42px;border:2px solid var(--ink);color:var(--ink);font-size:14px;display:flex;align-items:center;justify-content:center}

  /* hero */
  .hero{left:0;top:176px;width:1200px;height:443px;background:linear-gradient(100deg,#2f8fa0 0%,#6cc3cd 35%,#3a9bab 60%,#7fcbd3 100%)}
  .hero-kicker{left:704px;top:297px;width:302px;height:56px;background:var(--red);color:var(--white);font-size:34px;display:flex;align-items:center;justify-content:center}
  .hero-title{left:609px;top:359px;width:493px;height:80px;background:var(--red);color:var(--white);font-size:50px;line-height:80px;display:flex;align-items:center;justify-content:center;overflow:hidden}
  .ribbon{display:block}
  .ribbon-wrap{display:flex;align-items:center;justify-content:center}
  .ribbon-wrap span{position:absolute;color:var(--white)}

  /* boxed titles */
  .boxed{height:56px;border:2px solid currentColor;display:flex;align-items:center;justify-content:center;font-size:25px}

  /* portfolio */
  .intro{left:110px;top:790px;width:980px;text-align:center;font-size:13px;line-height:24px;color:var(--body)}
  .shot{top:895px;width:287px;height:387px}

  /* choose */
  .choose{left:0;top:1540px;width:1200px;height:635px;background:var(--brown)}
  .feature{width:318px;color:var(--white)}
  .feature .num{position:absolute;left:0;top:0;width:44px;height:44px;background:var(--white);color:var(--brown);font-size:30px;display:flex;align-items:center;justify-content:center}
  .feature h3{position:absolute;left:62px;top:8px;font-size:21px;color:var(--white)}
  .feature .rule{position:absolute;left:62px;top:40px;width:44px;height:3px;background:var(--white)}
  .feature p{position:absolute;left:0;top:64px;width:318px;font-size:14px;line-height:23px}
  .feature .more{position:absolute;left:0;top:139px;font-size:15px}

  /* testimonial */
  .t-name{left:152px;top:2398px;font-size:20px;color:var(--ink)}
  .t-rule{left:152px;top:2428px;width:82px;height:3px;background:var(--red)}
  .t-text{left:152px;top:2448px;width:515px;font-size:14px;line-height:23px}
  .arrow{top:2541px;width:44px;height:42px;background:var(--grey-btn);display:flex;align-items:center;justify-content:center}
  .product{left:717px;top:2366px;width:346px;height:217px;background:linear-gradient(120deg,#3a3430 0%,#b58f7a 45%,#e7d3c6 70%,#5c4b43 100%)}

  /* footer */
  .footer{left:0;top:2645px;width:1200px;height:361px;background:var(--footer)}
  .fcol{top:2645px;width:335px;height:315px;background:var(--brown-panel)}
  .fcol .fhead{height:98px;background:var(--red);color:var(--white);font-size:25px;display:flex;align-items:center;justify-content:center}
  .fcol.mid .fhead{background:var(--red-deep)}
  .fcol .dash{position:absolute;left:146px;top:128px;width:44px;height:2px;background:var(--white)}
  .fcol p{position:absolute;left:20px;top:150px;width:295px;text-align:center;font-size:14px;line-height:23px;color:var(--white)}
  .fcol .fbtn{position:absolute;left:100px;top:247px;width:135px;height:40px;border:2px solid var(--white);color:var(--white);font-size:14px;display:flex;align-items:center;justify-content:center}
  .news-input{position:absolute;left:41px;top:188px;width:181px;height:36px;border:2px solid var(--white);background:transparent}
  .news-send{position:absolute;left:222px;top:188px;width:75px;height:36px;background:var(--grey-btn);color:var(--ink);font-size:15px;display:flex;align-items:center;justify-content:center}

  .bottombar{left:0;top:3006px;width:1200px;height:91px;background:var(--bottom);color:var(--white);font-size:14px}
  .bottombar .copy{position:absolute;left:95px;top:0;line-height:91px}
  .bottombar .links{position:absolute;left:446px;top:0;line-height:91px;display:flex;gap:26px}
  .bottombar .social{position:absolute;left:921px;top:32px;display:flex;gap:12px}
  .bottombar .social span{width:26px;height:26px;display:block}
</style>
</head>
<body>
<div class="canvas">

  <!-- top bar -->
  <div class="abs topbar">
    <div class="abs welcome cond">Welcome to our site visitors</div>
    <nav class="abs nav cond"><span>Home</span><span>About me</span><span>My services</span><span>Contact</span></nav>
    <div class="abs search">
      <svg width="16" height="16" viewBox="0 0 16 16"><circle cx="6.5" cy="6.5" r="4.5" fill="none" stroke="#fff" stroke-width="2"/><line x1="10" y1="10" x2="14" y2="14" stroke="#fff" stroke-width="2"/></svg>
    </div>
  </div>

  <!-- header -->
  <div class="abs logo cond">Yourlogo</div>
  <div class="abs head-btn cond" style="left:761px;width:186px">Book appointments</div>
  <div class="abs head-btn cond" style="left:962px;width:142px">Make a deposit</div>

  <!-- hero -->
  <div class="abs hero" role="img" aria-label="Portrait of a woman with glamorous makeup wrapped in teal fabric"></div>
  <div class="abs hero-kicker cond">Doloremque</div>
  <div class="abs hero-title cond">Iam aut aspernatur</div>
  <div class="abs ribbon-wrap" style="left:753px;top:446px;width:207px;height:52px">
    <svg class="ribbon" width="207" height="52" viewBox="0 0 207 52"><polygon points="0,0 207,0 190,52 17,52" fill="#d8313a"/></svg>
    <span class="cond" style="font-size:26px">Read more</span>
  </div>

  <!-- portfolio -->
  <div class="abs boxed cond" style="left:485px;top:689px;width:230px;color:var(--ink)">My portfolio</div>
  <p class="abs intro">Lorem ipsum dolor sit amet rem eos illo omnis aut aperiam ab ipsam ipsa odit aut aperiam aut asperatur veritatis unde sed enim accusantium laudantium sunt perspiciatis ipsam sed doloremque ipsam dolores totam unde aut illo aut veritatis explicabo dicta quia dicta veritatis dicta sunt quasi eaque rem</p>
  <div class="abs shot" style="left:126px;background:linear-gradient(160deg,#4a2f22,#b7866b 55%,#e9d3c3)" role="img" aria-label="Portfolio photo: bridal makeup look with side-swept curls"></div>
  <div class="abs shot" style="left:457px;background:linear-gradient(160deg,#c7b9a4,#8e7459 55%,#e2d6c6)" role="img" aria-label="Portfolio photo: natural makeup look with knit scarf"></div>
  <div class="abs shot" style="left:787px;background:linear-gradient(160deg,#d9cbbd,#a6704b 50%,#efe4da)" role="img" aria-label="Portfolio photo: editorial eye makeup with pearl necklace"></div>
  <div class="abs ribbon-wrap" style="left:493px;top:1380px;width:211px;height:55px">
    <svg class="ribbon" width="211" height="55" viewBox="0 0 211 55"><polygon points="0,0 211,0 194,55 17,55" fill="#d8313a"/></svg>
    <span class="cond" style="font-size:26px">Read more</span>
  </div>

  <!-- what you choose me -->
  <div class="abs choose">
    <div class="abs boxed cond" style="left:436px;top:83px;width:325px;color:var(--white)">What you choose me</div>

    <div class="abs feature" style="left:95px;top:202px;height:170px">
      <div class="num cond">1</div><h3 class="cond">Amet voluptatem</h3><div class="rule"></div>
      <p>Lorem ipsum dolor sit amet rem illo omnis aperiam ab ipsam ipsa odit aut aperiam aut asperatur veritatis unde enim accusantium laudantium sunt</p>
      <div class="more cond">Read more</div>
    </div>
    <div class="abs feature" style="left:452px;top:202px;height:170px">
      <div class="num cond">2</div><h3 class="cond">Amet voluptatem</h3><div class="rule"></div>
      <p>Lorem ipsum dolor sit amet rem illo omnis aperiam ab ipsam ipsa odit aut aperiam aut asperatur veritatis unde enim accusantium laudantium sunt</p>
      <div class="more cond">Read more</div>
    </div>
    <div class="abs feature" style="left:805px;top:202px;height:170px">
      <div class="num cond">3</div><h3 class="cond">Amet voluptatem</h3><div class="rule"></div>
      <p>Lorem ipsum dolor sit amet rem illo omnis aperiam ab ipsam ipsa odit aut aperiam aut asperatur veritatis unde enim accusantium laudantium sunt</p>
      <div class="more cond">Read more</div>
    </div>
    <div class="abs feature" style="left:95px;top:410px;height:170px">
      <div class="num cond">4</div><h3 class="cond">Amet voluptatem</h3><div class="rule"></div>
      <p>Lorem ipsum dolor sit amet rem illo omnis aperiam ab ipsam ipsa odit aut aperiam aut asperatur veritatis unde enim accusantium laudantium sunt</p>
      <div class="more cond">Read more</div>
    </div>
    <div class="abs feature" style="left:452px;top:410px;height:170px">
      <div class="num cond">5</div><h3 class="cond">Amet voluptatem</h3><div class="rule"></div>
      <p>Lorem ipsum dolor sit amet rem illo omnis aperiam ab ipsam ipsa odit aut aperiam aut asperatur veritatis unde enim accusantium laudantium sunt</p>
      <div class="more cond">Read more</div>
    </div>
    <div class="abs feature" style="left:805px;top:410px;height:170px">
      <div class="num cond">6</div><h3 class="cond">Amet voluptatem</h3><div class="rule"></div>
      <p>Lorem ipsum dolor sit amet rem illo omnis aperiam ab ipsam ipsa odit aut aperiam aut asperatur veritatis unde enim accusantium laudantium sunt</p>
      <div class="more cond">Read more</div>
    </div>
  </div>

  <!-- testimonial & product -->
  <div class="abs boxed cond" style="left:258px;top:2247px;width:261px;color:var(--ink)">What they says</div>
  <div class="abs boxed cond" style="left:748px;top:2247px;width:284px;color:var(--ink)">Highlights product</div>
  <div class="abs t-name cond">Maya Doe, 25 yo</div>
  <div class="abs t-rule"></div>
  <p class="abs t-text">Lorem ipsum dolor sit amet rem eos illo omnis aut aperiam ab ipsam ipsa odit aperiam aut asperatur veritatis unde enim, sed enim accusantium laudantium sunt perspiciatis ipsam sed doloremque .....</p>
  <div class="abs arrow" style="left:544px">
    <svg width="14" height="20" viewBox="0 0 14 20"><polyline points="11,2 3,10 11,18" fill="none" stroke="#fff" stroke-width="3"/></svg>
  </div>
  <div class="abs arrow" style="left:593px">
    <svg width="14" height="20" viewBox="0 0 14 20"><polyline points="3,2 11,10 3,18" fill="none" stroke="#fff" stroke-width="3"/></svg>
  </div>
  <div class="abs product" role="img" aria-label="Product photo: makeup artist applying powder with a brush"></div>

  <!-- footer -->
  <div class="abs footer"></div>
  <div class="abs fcol" style="left:95px">
    <div class="fhead cond">About us</div>
    <div class="dash"></div>
    <p>Lorem ipsum dolor sit amet omnis aperiam ab ipsam ipsa odit aut aperiam aut asperatur veritatis unde enim accusantium laudantium</p>
    <div class="fbtn cond">Read more</div>
  </div>
  <div class="abs fcol mid" style="left:431px">
    <div class="fhead cond">Company address</div>
    <div class="dash"></div>
    <p>Lorem ipsum dolor sit amet omnis aperiam ab ipsam ipsa odit aut aperiam aut asperatur veritatis unde enim accusantium laudantium</p>
    <div class="fbtn cond">Read more</div>
  </div>
  <div class="abs fcol" style="left:766px;width:338px">
    <div class="fhead cond">Newsletter</div>
    <div class="dash"></div>
    <p style="top:148px">Lorem ipsum dolor sit amet omnis aperiam</p>
    <div class="news-input"></div>
    <div class="news-send cond">Send</div>
    <p style="top:246px">ab ipsam ipsa odit aut aperiam aut asperatur veritatis unde enim accusantium laudantium</p>
  </div>

  <div class="abs bottombar">
    <div class="copy">© 2014 <b>YOUR COMPANY</b>. ALL RIGHTS RESERVED.</div>
    <div class="links cond" style="font-weight:400"><span>About us</span><span>Term and use</span><span>Privacy policy</span><span>FAQs</span><span>Contact us</span></div>
    <div class="social">
      <span style="background:#3b5d9e"></span>
      <span style="background:#2ba3e0"></span>
      <span style="background:#d63a2f"></span>
      <span style="background:#2d78b3"></span>
      <span style="background:#d0272f"></span>
    </div>
  </div>

</div>
</body>
</html>
```